White Paper and One-Page Advertisement for TELVAMORE-QX

I need both documents to be better formatted and designed so they look professional, not something someone with mediocre word skills put together. They will go out to 1000s of industry professionals, and they need to look sharp. I need them to have my company's color palate logo, and branding on it similar to how it is now, but better. Please do not change any of the written content, but it can be arranged in any other format you think is better. Smart art and things i've already used can be omitted in favor of better designs. The developer is free to use their creativity. White paper should not be longer than the three pages unless necessary.

Target Market(s)

Life Sciences supply chain professionals

Colors
33b8a4
0592cd
9bcb3c
fbee3e
3277b5

Requirements
Must have
• Must be professional looking and not look like something done in word. Please use the color palate as seen on the documents.
Should not have
• Any changes to the written content.

```html
<!DOCTYPE html>
<html lang="en">
<head>
<meta charset="utf-8">
<title>TELVAMORE-QX — Refined Problem &amp; Paradigm Shift</title>
<link href="https://fonts.googleapis.com/css2?family=Source+Sans+3:ital,wght@0,400;0,600;0,700;1,700&display=swap" rel="stylesheet">
<style>
  :root{
    --teal:#33b8a4;
    --blue:#0592cd;
    --green:#9bcb3c;
    --yellow:#fbee3e;
    --steel:#3277b5;
    --paper:#e8f5f1;
    --ink:#1b1b1b;
    --frame:#2a2a2a;
  }
  *{box-sizing:border-box;margin:0;padding:0}
  html,body{width:848px;height:1200px;overflow:hidden;background:#fff}
  body{font-family:"Source Sans 3",Arial,sans-serif;color:var(--ink);font-size:11.5px;line-height:14px}
  .page{position:relative;width:848px;height:1200px;background:var(--paper);border:1px solid var(--frame);overflow:hidden}
  .abs{position:absolute}

  .rule{position:absolute;left:32px;height:4px}
  .rule--teal{top:64px;width:636px;background:var(--teal)}
  .rule--blue{top:83px;width:630px;background:var(--blue)}
  .rule--green{top:102px;width:624px;background:var(--green)}
  .rule--yellow{top:122px;width:630px;background:var(--yellow)}
  .rule--steel{top:141px;width:636px;background:var(--steel)}

  .brand{position:absolute;left:676px;top:42px;width:138px;height:96px;display:flex;flex-direction:column;align-items:center;justify-content:center;gap:6px}
  .brand__dot{width:40px;height:40px;border-radius:50%;background:var(--teal)}
  .brand__name{font-weight:700;font-size:15px;color:var(--teal);letter-spacing:.5px}

  .band{position:absolute;left:32px;width:782px;height:28px;background:var(--teal);color:#fff;font-weight:600;font-size:17px;letter-spacing:1px;text-align:center;line-height:28px}
  .band--refined{top:182px}
  .band--root{top:569px}
  .section-end{position:absolute;left:32px;width:782px;height:2px;background:var(--teal)}

  .vdivider{position:absolute;width:2px;background:var(--teal)}

  p.body{text-align:justify}
  h3{font-size:14px;font-weight:700;line-height:17px;margin-top:3px}
  h3.italic{font-style:italic}
  .hl{color:var(--teal)}

  ul.dots{list-style:none}
  ul.dots li{position:relative;padding-left:16px}
  ul.dots li::before{content:"";position:absolute;left:1px;top:3px;width:9px;height:9px;border-radius:50%;background:var(--yellow)}
  ul.benefits{font-size:11px}

  .barrier{position:absolute;left:0;width:478px}
  .barrier__tag{height:15px;border-radius:8px;color:#fff;font-weight:600;font-size:12px;line-height:15px;padding-left:16px}
  .barrier__tag--green{background:var(--green)}
  .barrier__tag--yellow{background:var(--yellow)}
  .barrier__tag--teal{background:var(--teal)}
  .barrier__tag--blue{background:var(--blue)}
  .barrier__tag--steel{background:var(--steel)}
  .barrier__text{position:relative;padding:1px 0 0 32px;text-align:justify}
  .barrier__text::before{content:"";position:absolute;left:24px;top:7px;width:5px;height:5px;border-radius:50%;background:var(--ink)}

  .vision{position:absolute;left:379px;top:614px;width:432px;height:120px}
  .vision svg{position:absolute;left:0;top:0}
  .vision ol{position:absolute;left:36px;top:22px;width:340px;color:#fff;font-weight:600;font-size:11.5px;line-height:14px;padding-left:14px}

  .tagline{position:absolute;left:0;width:848px;top:980px;text-align:center;color:var(--teal);font-weight:700;font-size:13px}
  .tagline u{text-underline-offset:2px}

  .photo{position:absolute;top:997px;height:156px}
</style>
</head>
<body>
<main class="page">
  <div class="rule rule--teal"></div>
  <div class="rule rule--blue"></div>
  <div class="rule rule--green"></div>
  <div class="rule rule--yellow"></div>
  <div class="rule rule--steel"></div>

  <div class="brand">
    <span class="brand__dot"></span>
    <span class="brand__name">TELVAMORE-QX</span>
  </div>

  <div class="band band--refined">REFINED PROBLEM</div>

  <section class="abs" style="left:32px;top:210px;width:290px">
    <p class="body">There is no clear market leader that helps organizations optimize waste, collaborative to reduce it, and market more quality materials to more firms whether for research, manufacturing, or donations. This marketplace must be regulated and all participates properly vetted and authenticated. Accounts must be created to enable companies to post materials and request for information/quotes. Additionally, this marketplace must facilitate collaborative relationships between companies that help them reduce supply chain costs. It must quickly, economically, compliantly, and legally facilitate those exchanges. Lack of this market leader may have enabled the waste problem as seen today.</p>
    <h3>Contemporary Operating Environment</h3>
    <ul class="dots">
      <li>Constant pressure from global competition, increasing customer and governmental demand on price, more regulatory scrutiny, and a relentless societal pursuit of sustainability are starting to erode what were once high margins for Pharma6.</li>
      <li>Regulators are cooperative and open to solutions.</li>
      <li>Exchanges and consortiums are not typically leveraged in Pharma.</li>
      <li>Pharma continues to struggle with the bullwhip effect.</li>
    </ul>
  </section>

  <div class="vdivider" style="left:326px;top:210px;height:338px"></div>

  <section class="abs" style="left:336px;top:210px;width:478px;height:338px">
    <h3 style="margin-top:0">Barriers</h3>
    <div class="barrier" style="top:25px"><div class="barrier__tag barrier__tag--green">Compliance</div>
      <p class="barrier__text">It is the responsibility of manufacturers to provide customers/patients with quality, safe, and efficacious products. However, there is a misperception that high quality cGMP compliant materials, parts, and equipment cannot be sourced from aftermarket exchanges and consortiums.</p></div>
    <div class="barrier" style="top:101px"><div class="barrier__tag barrier__tag--yellow">Liability</div>
      <p class="barrier__text">Contractual agreements with suppliers have clauses to resolve issues dealing with poor quality. There is a misperception that these agreements cannot implemented at both the marketplace and transactionactional level.</p></div>
    <div class="barrier" style="top:163px"><div class="barrier__tag barrier__tag--teal">Economics</div>
      <p class="barrier__text">Exchanges can be difficult due to time/effort. A sanctioned marketplace can provide the structure to make it easy.</p></div>
    <div class="barrier" style="top:211px"><div class="barrier__tag barrier__tag--blue">Sustainability</div>
      <p class="barrier__text">Firms have not discovered how to leverage exchanges to reduce environmental footprint and enable industry certifications as well as community trust.</p></div>
    <div class="barrier" style="top:259px"><div class="barrier__tag barrier__tag--steel">Confidence</div>
      <p class="barrier__text">Trust is critical to firms. They should know that a marketplace has properly vetted members with KPI data for analysis.</p></div>
    <div class="barrier" style="top:307px"><div class="barrier__tag barrier__tag--green">Speed</div>
      <p class="barrier__text">Exchanges should be fast. An innovative marketplace can ensure quick exchanges.</p></div>
  </section>

  <div class="section-end" style="top:547px"></div>

  <div class="band band--root">ROOT CAUSE &amp; PARADIGM SHIFT</div>

  <section class="abs" style="left:32px;top:599px;width:333px">
    <p class="body">so high, it hasn’t been a priority to solve. Additionally, there hasn’t been an effective means to deal with waste. This limits the industry’s ability to leverage these marketplaces. Finally, misperceived issues or liability and quality have strained innovation; all solvable problems.</p>
    <h3>Future State</h3>
    <p class="body">Creation of <span class="hl">Private Virtual Life Sciences Multi-Vendor Marketplace &amp; Consortium</span> where researchers, manufacturers, and original-end manufacturers can create a simple storefront for their organization and transact materials, equipment, parts, and collaborative relationships in a compliant and professional environment. This marketplace uses a series of software logic that leverages auditing capabilities of buyers and sellers by making FDA required data and documentation visible and subject to ALCOA-Plus, thus enabling transactions in a fast and compliant manner. This logic then automates contracts for digital signature in a part 11 compliant package.</p>
    <h3>Benefits</h3>
    <ul class="dots benefits">
      <li>Avoid write-downs for surplus material/consumable stock</li>
      <li>Continue production when stocked-out of materials</li>
      <li>Reduce purchase price of materials</li>
      <li>Risk pool safety stock to reduce amount required</li>
      <li>Allow for leaner planning in that stock-outs can be addressed</li>
      <li>Allow for more responsive planning with an outlet to sell SS</li>
      <li>Reduce supplier audit resources and costs</li>
      <li>Reduce environment footprint by avoiding disposal fees</li>
    </ul>
  </section>

  <div class="vdivider" style="left:370px;top:599px;height:376px"></div>

  <section class="abs" style="left:379px;top:599px;width:435px">
    <h3 style="margin-top:0">Vision</h3>
  </section>
  <div class="vision">
    <svg width="432" height="120" viewBox="0 0 432 120" aria-hidden="true">
      <g fill="#0592cd">
        <ellipse cx="216" cy="62" rx="200" ry="44"/>
        <ellipse cx="80" cy="52" rx="74" ry="40"/>
        <ellipse cx="190" cy="36" rx="110" ry="32"/>
        <ellipse cx="330" cy="42" rx="86" ry="36"/>
        <ellipse cx="120" cy="84" rx="100" ry="32"/>
        <ellipse cx="300" cy="84" rx="110" ry="32"/>
        <ellipse cx="395" cy="68" rx="34" ry="30"/>
      </g>
    </svg>
    <ol>
      <li>A collaborative and compliant multi-vendor marketplace is part of Pharma’s normal operating practices</li>
      <li>Waste is not tolerated in the life sciences industry</li>
      <li>There is always a compliant outlet to procure and transact before and after market materials</li>
    </ol>
  </div>

  <section class="abs" style="left:379px;top:742px;width:435px">
    <h3 style="margin-top:0">How to Implement</h3>
    <p class="body">Application of the following guidance, regulations, and bodies will drive exchange process and design:</p>
    <ul class="dots" style="padding-left:16px">
      <li>ICH Q7 (international harmonized cGMP standards)</li>
      <li>CFR Title 21 (US cGMP standards)</li>
      <li>Data Integrity Draft Guidance by FDA (good doc practices)</li>
      <li>WHO GMP for Pharmaceutical Products (World Health Organizations cGMP standards)</li>
      <li>APIC - Good Manufacturing Practices in Active Pharmaceutical Ingredients Development, 1999.</li>
      <li>APIC Supplier Qualification and Management Guidelines</li>
    </ul>
    <h3 class="italic">Data Integrity</h3>
    <p class="body">Data integrity will drive how the exchange operates. All parties are encouraged to use the FDA’s ALCOA-Plus system to review documents associated with transactions. This enables buyers’ standards of data integrity and cGMP quality compliance to be adhered.</p>
  </section>

  <p class="tagline">Every new journey of change and innovation we take is for them... <u>The Patient</u></p>

  <div class="photo" style="left:34px;width:252px;background:linear-gradient(135deg,#d9cfc6,#a89a8c)" role="img" aria-label="Photo of a smiling baby in a knitted hat"></div>
  <div class="photo" style="left:289px;width:252px;background:linear-gradient(135deg,#6f7a52,#3b3a2c)" role="img" aria-label="Photo of a smiling young woman outdoors"></div>
  <div class="photo" style="left:544px;width:268px;background:linear-gradient(135deg,#b08a5a,#5a6a8a)" role="img" aria-label="Photo of a smiling elderly woman with glasses"></div>
</main>
</body>
</html>
```